Business Card Design Project

Im an electrician and my company name is Kestrel Electrical
My main work is installing Lighting and Power Points, Home Theater Systems, TVS, Phones and Data
Im looking a business card, something nice, clean, modern and not to cluttered
Im open to sugestions
I dont mind if the "Services" is on the back on the business card
colours black, grey, white or the blue colour of my logo are prefered but not compulsory
any questions just message me
and please make it so if i need to edit the writing can do it easy. maybe by making it a seperate layer ?
My Details are.
Name - Peter Halloran
Job Title - Licenced Electrician
Mobile - 027 583 2174
Email - peter@kestrelelectrical.co.nz
Web - www.kestrelelectrical.co.nz
Services
Residential / Commercial
Lighting & Power
Heating & Ventilation
Automation
Phone & Data
Home Cinema
Sound Systems
TV, Antenna & Satellite
Digital Upgrades

```html
<!DOCTYPE html>
<html lang="en">
<head>
<meta charset="utf-8">
<title>Kestrel Electrical – Business Card</title>
<link rel="stylesheet" href="https://fonts.googleapis.com/css2?family=Jost:wght@500;800&family=Oswald:wght@300;400&display=swap">
<style>
  :root {
    --page: #ffffff;
    --card: #1e1e1d;
    --label: #ffffff;
    --ink: #161616;
    --brand-blue: #4aa8c9;
  }
  * { margin: 0; padding: 0; box-sizing: border-box; }
  html, body {
    width: 1200px; height: 1000px; overflow: hidden;
    background: var(--page);
  }
  .canvas { position: relative; width: 1200px; height: 1000px; }

  .card {
    position: absolute; top: 148px;
    width: 402px; height: 704px;
    background: var(--card);
  }
  .card--front { left: 95px; }
  .card--back  { left: 700px; }

  .brand {
    position: absolute; left: 32px; top: 172px;
    display: flex; align-items: center; gap: 16px;
  }
  .brand__mark {
    width: 58px; height: 58px; background: var(--brand-blue);
  }
  .brand__name {
    font-family: "Jost", sans-serif; font-weight: 500;
    color: var(--brand-blue);
    font-size: 31px; line-height: 1.05; letter-spacing: 1px;
    text-transform: uppercase;
  }

  .label-list { position: absolute; left: 16px; top: 410px; list-style: none; }
  .label {
    position: absolute; left: 0;
    width: 367px; height: 36px;
    background: var(--label); color: var(--ink);
    display: flex; align-items: center;
    white-space: nowrap;
  }
  .label:nth-child(1) { top: 0; }
  .label:nth-child(2) { top: 67px; }
  .label:nth-child(3) { top: 133px; }
  .label:nth-child(4) { top: 202px; }

  .label--service {
    padding-left: 15px;
    font-family: "Jost", sans-serif; font-weight: 800;
    font-size: 19px; letter-spacing: 0.3px;
  }
  .label--web { font-size: 16px; letter-spacing: 0.6px; }

  .label--contact {
    padding-left: 14px;
    font-family: "Oswald", sans-serif; font-weight: 300;
    font-size: 23px;
  }
  .label__icon {
    width: 26px; height: 22px; margin-right: 13px;
    display: flex; align-items: center; justify-content: center;
    flex: none;
  }
  .label__icon svg { fill: var(--ink); }
  .label--email { font-size: 22px; text-transform: uppercase; }
</style>
</head>
<body>
<main class="canvas">

  <section class="card card--front" aria-label="Card front">
    <div class="brand">
      <span class="brand__mark"></span>
      <span class="brand__name">Kestrel<br>Electrical</span>
    </div>
    <ul class="label-list">
      <li class="label label--service">Lighting and Power Points</li>
      <li class="label label--service">Home Theater Systems and TV’s</li>
      <li class="label label--service">Phones and Data</li>
      <li class="label label--service label--web">WWW.KESTRELELECTRICAL.CO.NZ</li>
    </ul>
  </section>

  <section class="card card--back" aria-label="Card back">
    <ul class="label-list">
      <li class="label label--contact">
        <span class="label__icon"><svg width="20" height="20" viewBox="0 0 20 20"><circle cx="10" cy="5.5" r="4.5"/><path d="M1 20c0-5 4-8 9-8s9 3 9 8z"/></svg></span>
        Peter Halloran
      </li>
      <li class="label label--contact">
        <span class="label__icon"><svg width="12" height="20" viewBox="0 0 12 20"><path d="M7 0 1 11h4l-2 9 8-12H7l3-8z"/></svg></span>
        Licenced Electrician
      </li>
      <li class="label label--contact">
        <span class="label__icon"><svg width="12" height="20" viewBox="0 0 12 20"><path d="M2 3h8a2 2 0 0 1 2 2v13a2 2 0 0 1-2 2H2a2 2 0 0 1-2-2V5a2 2 0 0 1 2-2zm0 3v6h8V6zM3 0h2v3H3z"/></svg></span>
        027 583 2174
      </li>
      <li class="label label--contact label--email">
        <span class="label__icon"><svg width="26" height="18" viewBox="0 0 26 18"><path d="M1 1h24v16H1z" fill="none" stroke="#161616" stroke-width="2"/><path d="M1 1l12 10L25 1" fill="none" stroke="#161616" stroke-width="2"/></svg></span>
        peter@kestrelelectrical.co.nz
      </li>
    </ul>
  </section>

</main>
</body>
</html>
```